infographic series

To convert each of the below pieces of information into a graphic for facebook.
The 07 figure should be blue and the 2012 figure should be red.
The audience is Australian, female and aged 25-45 with dependent children.
These should be provided both as four separate infographics and as one which includes all three figures.
Early childhood and child care budget
2012 $22.3 billion
2007 $7.3 billion
Homestart Bonus
2007 $4,354
2012 $7,500
Families using approved child care
2007 571,900
2012 929,000 (62.4% increase)
Approved child care services
2007 11,266
2012 16,000
women aged 25-45 with young kids skimming their facebook newsfeed

```html
<!DOCTYPE html>
<html lang="en">
<head>
<meta charset="utf-8">
<title>Child Care Infographic Series</title>
<link rel="stylesheet" href="https://fonts.googleapis.com/css2?family=Oswald:wght@400;700&family=Archivo:wght@700;800&display=swap">
<style>
  :root {
    --canvas: #ffffff;
    --panel: #e3e3e3;
    --bar: #7d7d7d;
    --bar-dark: #5e5e5e;
    --red: #c8202a;
    --blue: #2e4d9c;
    --grey-figure: #8c8c8c;
    --caption: #222222;
  }
  * { box-sizing: border-box; margin: 0; padding: 0; }
  html, body { width: 831px; height: 1200px; overflow: hidden; background: var(--canvas); }
  body { position: relative; font-family: "Archivo", Arial, sans-serif; }

  .size-label {
    position: absolute; left: 0; width: 831px; text-align: center;
    font: 700 14px "Archivo", Arial, sans-serif; color: var(--caption);
  }

  .board {
    position: absolute;
    background: linear-gradient(160deg, #ececec, var(--panel) 55%, #dadada);
    box-shadow: 3px 4px 6px rgba(0,0,0,.45);
    overflow: hidden;
  }
  .board--hero { left: 102px; top: 19px; width: 640px; height: 448px; --u: 10px; }
  .board--small { top: 518px; width: 256px; height: 179px; --u: 4px; }
  .board--combined { left: 100px; top: 739px; width: 641px; height: 450px; }

  .stat { position: absolute; inset: 0; overflow: hidden; }
  .combined-cell { position: absolute; width: 296px; height: 206px; --u: 4.6px; }

  .stat-title {
    position: absolute; left: 0; right: 0; top: 0; height: calc(var(--u) * 5);
    display: flex; align-items: center; justify-content: center;
    background: linear-gradient(var(--bar), var(--bar-dark));
    color: #fff; font: 400 calc(var(--u) * 2.2) / 1 "Oswald", Arial, sans-serif;
    text-transform: uppercase; white-space: nowrap; letter-spacing: .02em;
  }
  .stat-base {
    position: absolute; left: 0; right: 0; bottom: 0; height: calc(var(--u) * 1.2);
    background: var(--bar);
  }

  .year {
    position: absolute; top: calc(var(--u) * 7.5); writing-mode: vertical-rl;
    font: 700 calc(var(--u) * 12.5) / 1 "Oswald", Arial, sans-serif;
    text-shadow: 1px 2px 3px rgba(0,0,0,.35); white-space: nowrap;
  }
  .year--2012 { left: calc(var(--u) * 1.3); color: var(--red); transform: rotate(180deg); }
  .year--2007 { right: calc(var(--u) * 1.3); color: var(--blue); }

  .figure-art {
    position: absolute; top: calc(var(--u) * 8.5);
    width: calc(var(--u) * 16); height: calc(var(--u) * 25);
    border-radius: 40% 40% 8% 8%;
  }
  .figure-art--2012 { left: calc(var(--u) * 13.5); background: linear-gradient(var(--grey-figure) 25%, var(--red) 85%); }
  .figure-art--2007 { left: calc(var(--u) * 33); background: linear-gradient(var(--grey-figure) 35%, var(--blue) 88%); }

  .value {
    position: absolute; top: calc(var(--u) * 34.8); z-index: 1;
    font: 800 calc(var(--u) * 3.2) / 1.05 "Archivo", Arial, sans-serif;
    white-space: nowrap; text-shadow: 1px 1px 1px rgba(0,0,0,.25);
  }
  .value--2012 { left: calc(var(--u) * 4.5); color: var(--red); }
  .value--2007 { left: calc(var(--u) * 34.5); color: var(--blue); }
  .value small { display: block; font-size: .6em; font-weight: 700; }
</style>
</head>
<body>

  <section class="board board--hero">
    <div class="stat">
      <h2 class="stat-title">Families using approved child care</h2>
      <span class="year year--2012">2012</span>
      <div class="figure-art figure-art--2012" role="img" aria-label="Silhouette of a parent holding two children, grey fading to red"></div>
      <div class="figure-art figure-art--2007" role="img" aria-label="Silhouette of a parent holding two children, grey fading to blue"></div>
      <span class="year year--2007">2007</span>
      <p class="value value--2012">929,000<small>(62.4% increase)</small></p>
      <p class="value value--2007">571,900</p>
      <div class="stat-base"></div>
    </div>
  </section>

  <p class="size-label" style="top:478px">720 x 504</p>

  <section class="board board--small" style="left:17px">
    <div class="stat">
      <h2 class="stat-title">Approved child care services</h2>
      <span class="year year--2012">2012</span>
      <div class="figure-art figure-art--2012" role="img" aria-label="Silhouette of a seated child, grey fading to red"></div>
      <div class="figure-art figure-art--2007" role="img" aria-label="Silhouette of a seated child, grey fading to blue"></div>
      <span class="year year--2007">2007</span>
      <p class="value value--2012">16,000</p>
      <p class="value value--2007">11,266</p>
      <div class="stat-base"></div>
    </div>
  </section>

  <section class="board board--small" style="left:288px">
    <div class="stat">
      <h2 class="stat-title">Early childhood &amp; child care budget</h2>
      <span class="year year--2012">2012</span>
      <div class="figure-art figure-art--2012" role="img" aria-label="Silhouette of a kneeling child, grey fading to red"></div>
      <div class="figure-art figure-art--2007" role="img" aria-label="Silhouette of a kneeling child, grey fading to blue"></div>
      <span class="year year--2007">2007</span>
      <p class="value value--2012">$22.3 billion</p>
      <p class="value value--2007">$7.3 billion</p>
      <div class="stat-base"></div>
    </div>
  </section>

  <section class="board board--small" style="left:558px">
    <div class="stat">
      <h2 class="stat-title">Homestart Bonus</h2>
      <span class="year year--2012">2012</span>
      <div class="figure-art figure-art--2012" role="img" aria-label="Silhouette of a toddler walking, grey fading to red"></div>
      <div class="figure-art figure-art--2007" role="img" aria-label="Silhouette of a toddler walking, grey fading to blue"></div>
      <span class="year year--2007">2007</span>
      <p class="value value--2012">$7,500</p>
      <p class="value value--2007">$4,354</p>
      <div class="stat-base"></div>
    </div>
  </section>

  <p class="size-label" style="top:712px">720 x 504</p>

  <section class="board board--combined">
    <div class="combined-cell" style="left:16px; top:12px">
      <div class="stat">
        <h2 class="stat-title">Early childhood &amp; child care budget</h2>
        <span class="year year--2012">2012</span>
        <div class="figure-art figure-art--2012" role="img" aria-label="Silhouette of a kneeling child, grey fading to red"></div>
        <div class="figure-art figure-art--2007" role="img" aria-label="Silhouette of a kneeling child, grey fading to blue"></div>
        <span class="year year--2007">2007</span>
        <p class="value value--2012">$22.3 billion</p>
        <p class="value value--2007">$7.3 billion</p>
        <div class="stat-base"></div>
      </div>
    </div>
    <div class="combined-cell" style="left:330px; top:12px">
      <div class="stat">
        <h2 class="stat-title">Homestart Bonus</h2>
        <span class="year year--2012">2012</span>
        <div class="figure-art figure-art--2012" role="img" aria-label="Silhouette of a toddler walking, grey fading to red"></div>
        <div class="figure-art figure-art--2007" role="img" aria-label="Silhouette of a toddler walking, grey fading to blue"></div>
        <span class="year year--2007">2007</span>
        <p class="value value--2012">$7,500</p>
        <p class="value value--2007">$4,354</p>
        <div class="stat-base"></div>
      </div>
    </div>
    <div class="combined-cell" style="left:16px; top:232px">
      <div class="stat">
        <h2 class="stat-title">Approved child care services</h2>
        <span class="year year--2012">2012</span>
        <div class="figure-art figure-art--2012" role="img" aria-label="Silhouette of a seated child, grey fading to red"></div>
        <div class="figure-art figure-art--2007" role="img" aria-label="Silhouette of a seated child, grey fading to blue"></div>
        <span class="year year--2007">2007</span>
        <p class="value value--2012">16,000</p>
        <p class="value value--2007">11,266</p>
        <div class="stat-base"></div>
      </div>
    </div>
    <div class="combined-cell" style="left:330px; top:232px">
      <div class="stat">
        <h2 class="stat-title">Families using approved child care</h2>
        <span class="year year--2012">2012</span>
        <div class="figure-art figure-art--2012" role="img" aria-label="Silhouette of a parent holding two children, grey fading to red"></div>
        <div class="figure-art figure-art--2007" role="img" aria-label="Silhouette of a parent holding two children, grey fading to blue"></div>
        <span class="year year--2007">2007</span>
        <p class="value value--2012">929,000<small>(62.4% increase)</small></p>
        <p class="value value--2007">571,900</p>
        <div class="stat-base"></div>
      </div>
    </div>
  </section>

</body>
</html>
```